Biography of the Prophet Zeravin

We need a great book cover which honors the Name of the Prophet Zeravin. It should be classic clean and has islamic elements. It is a book in german language. I attached the informations which should be placed on the front- and backcover.

Target Market(s)

Islamic. Germany.

Font styles to use
Serif

Colors

Designer to choose colors to be used in the design.

Requirements
Must have
• Must include all texts i've attached in the pdfs.

```html
<!DOCTYPE html>
<html lang="de">
<head>
<meta charset="utf-8">
<title>Zeravin – Buchcover</title>
<link rel="stylesheet" href="https://fonts.googleapis.com/css2?family=Lora:wght@700&family=Marcellus&family=EB+Garamond:ital@1&display=swap">
<style>
  :root {
    --backdrop: #ececec;
    --parchment-light: #caa56a;
    --parchment: #b08a52;
    --parchment-dark: #87653a;
    --title-brown: #5e1f08;
    --subtitle-brown: #6b2a10;
    --band: #6a220e;
    --band-text: #f3e4cf;
    --scene-light: #efe0c2;
    --scene-mid: #9c7c50;
    --scene-dark: #5a4327;
    --arch-line: rgba(246, 234, 212, 0.75);
  }
  * { margin: 0; padding: 0; box-sizing: border-box; }
  html, body {
    width: 1200px; height: 1200px; overflow: hidden;
    background: var(--backdrop);
  }
  .cover {
    position: absolute;
    left: 243px; top: 50px;
    width: 714px; height: 1100px;
    background:
      radial-gradient(ellipse at 50% 35%, var(--parchment-light) 0%, var(--parchment) 60%, var(--parchment-dark) 100%);
    overflow: hidden;
    box-shadow: 0 6px 24px rgba(0,0,0,0.25);
  }
  .cover-illustration {
    position: absolute;
    left: 0; top: 0; width: 714px; height: 660px;
    background:
      linear-gradient(160deg, rgba(255,246,225,0.55) 0%, rgba(255,246,225,0) 38%),
      radial-gradient(ellipse 30% 40% at 46% 52%, var(--scene-light) 0%, rgba(239,224,194,0) 75%),
      linear-gradient(180deg, var(--parchment-light) 0%, var(--parchment) 18%, var(--scene-mid) 32%, var(--scene-dark) 55%, var(--scene-mid) 75%, rgba(176,138,82,0) 100%);
  }
  .arch-frame {
    position: absolute;
    left: 0; top: 0; width: 714px; height: 660px;
  }
  .cover-title {
    position: absolute;
    left: 0; width: 100%; top: 512px;
    text-align: center;
    font-family: "Lora", serif;
    font-weight: 700;
    font-size: 120px;
    line-height: 1;
    letter-spacing: -1px;
    color: var(--title-brown);
  }
  .cover-subtitle {
    position: absolute;
    left: 0; width: 100%; top: 648px;
    text-align: center;
    font-family: "Marcellus", serif;
    font-size: 39px;
    line-height: 47px;
    color: var(--subtitle-brown);
  }
  .credit-band {
    position: absolute;
    left: 0; top: 800px; width: 100%; height: 106px;
    background: var(--band);
    display: flex; flex-direction: column; justify-content: center; align-items: center;
    font-family: "EB Garamond", serif;
    font-style: italic;
    font-size: 28px;
    line-height: 34px;
    color: var(--band-text);
  }
  .publisher {
    position: absolute;
    left: 0; width: 100%; top: 945px;
    display: flex; flex-direction: column; align-items: center; gap: 18px;
  }
  .publisher-mark {
    width: 56px; height: 56px;
    border: 2px solid var(--band-text);
  }
  .publisher-name {
    font-family: "Marcellus", serif;
    font-size: 17px;
    color: var(--band-text);
  }
</style>
</head>
<body>
  <main class="cover">
    <div class="cover-illustration" role="img" aria-label="Sepia scene of an old Arabian town with palm trees and a watchtower, light rays falling on large Arabic calligraphy of the prophet's name with a blessing above it"></div>

    <svg class="arch-frame" viewBox="0 0 714 660" aria-hidden="true">
      <path d="M232 500 L232 250 Q232 170 357 95 Q482 170 482 250 L482 500"
            fill="none" stroke="var(--arch-line)" stroke-width="2"/>
      <path d="M246 500 L246 254 Q246 184 357 112 Q468 184 468 254 L468 500"
            fill="none" stroke="var(--arch-line)" stroke-width="1"/>
      <line x1="200" y1="500" x2="514" y2="500" stroke="var(--arch-line)" stroke-width="1.5"/>
    </svg>

    <h1 class="cover-title">Zeravin</h1>

    <p class="cover-subtitle">
      Seine Lebensgeschichte,<br>
      Fakten aus seinem Alltag<br>
      und seine Besonderheiten
    </p>

    <div class="credit-band">
      <span>Von Abū al-Ḥasan Yūsuf ibn Ḫālid ibn Naṣīr</span>
      <span>Übersetzt und kommentiert von Tarik Rosenauer</span>
    </div>

    <div class="publisher">
      <div class="publisher-mark"></div>
      <span class="publisher-name">Nurhaus Verlag</span>
    </div>
  </main>
</body>
</html>
```